Design for sports training app

We need the design for 9 screens of an app that supports trainers of sport teams in preparing their training sessions. Regarding colors, fonts etc. there is absolute freedom for the designer to choose what he thinks is best.
The app will be called "Plomix", our idea for the logo is something like a stopwatch.
Wireframes are attached for every screen. You don't have to stick to those - if you have better ideas, we are happy to see them.
Our strategy is "mobile first". Based on the app design we will create a homepage later - I guess it makes sense to give this to the same person, let's see.
The deliverables are attached.
All in all the main target is to present a very simple, intuitive and nice UI that the user can work with without much learning.
Updates
Target Market(s)
Soccer trainers
Industry/Entity Type
Training
Look and feel

```html
<!DOCTYPE html>
<html lang="en">
<head>
<meta charset="utf-8">
<title>Plomix – Training Session</title>
<link href="https://fonts.googleapis.com/css2?family=Oswald:wght@300;400;500&family=Roboto:wght@400;500&display=swap" rel="stylesheet">
<style>
  :root {
    --page-bg: #f1f1f1;
    --screen-bg: #141518;
    --panel-bg: #1c1d21;
    --row-bg: #1d1e22;
    --row-gap: #121316;
    --text-main: #e4e5e7;
    --text-muted: #a4a6ab;
    --icon: #c9cacd;
    --ring-outer: #18191d;
    --ring-mid: #1c1d21;
    --ring-inner: #212227;
    --accent: #2aa3c4;
    --accent-deep: #1c6f9e;
  }
  * { box-sizing: border-box; margin: 0; padding: 0; }
  html, body { width: 1200px; height: 1200px; overflow: hidden; }
  body {
    background: var(--page-bg);
    font-family: "Oswald", "Arial Narrow", sans-serif;
    color: var(--text-main);
    position: relative;
  }
  .screen {
    position: absolute;
    left: 408px; top: 42px;
    width: 384px; height: 1116px;
    background: var(--screen-bg);
    overflow: hidden;
  }
  .status-bar {
    height: 36px;
    display: flex; align-items: center; justify-content: space-between;
    padding: 0 12px;
    font-family: "Roboto", Helvetica, sans-serif;
    font-size: 11px; color: #fff;
  }
  .status-left, .status-right { display: flex; align-items: center; gap: 4px; width: 110px; }
  .status-right { justify-content: flex-end; }
  .signal { letter-spacing: -1px; font-size: 9px; }
  .battery { width: 24px; height: 9px; border-radius: 2px; background: #fff; position: relative; }
  .battery::after { content: ""; position: absolute; right: -3px; top: 3px; width: 2px; height: 3px; background: #fff; }

  .app-header {
    height: 48px;
    display: flex; align-items: center; justify-content: center;
    position: relative;
    font-weight: 300; font-size: 19px; letter-spacing: 0.2px; color: var(--text-main);
  }
  .settings-icon { position: absolute; right: 22px; top: 12px; width: 24px; height: 24px; }

  .weather-card {
    margin: 3px 8px 0;
    height: 150px;
    background: var(--panel-bg);
    display: flex;
  }
  .weather-info { flex: 1; padding: 18px 0 0 28px; position: relative; }
  .weather-state { font-size: 21px; font-weight: 400; }
  .cloud { position: absolute; left: 112px; top: 22px; width: 64px; height: 38px; }
  .temp-line { display: flex; align-items: baseline; gap: 10px; margin-top: 8px; }
  .temp { font-size: 32px; font-weight: 400; line-height: 1; }
  .feels { font-size: 12px; font-weight: 300; color: var(--text-muted); }
  .precip { font-size: 14px; font-weight: 300; color: var(--text-muted); margin-top: 14px; }
  .date-block {
    width: 110px;
    border-left: 1px solid #26272c;
    display: flex; flex-direction: column; align-items: center; padding-top: 24px;
  }
  .calendar {
    width: 54px; height: 54px; border: 2px solid var(--text-main);
    display: flex; align-items: center; justify-content: center;
    font-size: 32px; font-weight: 400; position: relative; padding-top: 6px;
  }
  .calendar::before { content: ""; position: absolute; top: 0; left: 0; right: 0; height: 6px; background: #9a9ca1; }
  .month { font-size: 19px; font-weight: 300; margin-top: 4px; }
  .weekday { font-size: 12px; font-weight: 300; color: var(--text-muted); }

  .session-time {
    margin: 0 8px;
    height: 76px;
    background: #191a1e;
    display: flex; align-items: center; justify-content: center;
    font-size: 34px; font-weight: 400; letter-spacing: 0.5px;
  }

  .hero {
    height: 274px; position: relative;
    display: flex; align-items: center; justify-content: center;
  }
  .ring { position: absolute; border-radius: 50%; }
  .ring-outer { width: 216px; height: 216px; background: var(--ring-outer); }
  .ring-mid { width: 172px; height: 172px; background: var(--ring-mid); }
  .ring-inner { width: 136px; height: 136px; background: var(--ring-inner); }
  .hero-art {
    position: relative; width: 90px; height: 76px; border-radius: 38px;
    background: radial-gradient(circle at 50% 45%, var(--accent) 0%, var(--accent-deep) 60%, rgba(28,111,158,0) 100%);
    opacity: 0.85;
  }

  .session-list { display: flex; flex-direction: column; gap: 2px; background: var(--row-gap); }
  .drill-row {
    height: 78px; margin: 0 8px; background: var(--row-bg);
    display: flex; align-items: center; justify-content: space-between;
    padding: 0 30px 0 30px;
  }
  .drill-name { font-size: 19px; font-weight: 400; line-height: 1.1; }
  .drill-name small { font-size: 14px; }
  .drill-duration { font-size: 13px; font-weight: 400; color: var(--text-muted); margin-top: 2px; }
  .nav-title { font-size: 19px; font-weight: 400; }
  .row-icon { width: 28px; height: 28px; }

  .app-footer {
    position: absolute; bottom: 0; left: 0; right: 0; height: 56px;
    display: flex; align-items: center; justify-content: center;
  }
  .footer-mark { width: 10px; height: 10px; border-radius: 50%; background: #2a2b30; }
</style>
</head>
<body>
  <main class="screen">
    <div class="status-bar">
      <div class="status-left"><span class="signal">●●●○○</span><span>NOVA</span>
        <svg width="12" height="9" viewBox="0 0 12 9"><path d="M1 3.5a7 7 0 0 1 10 0M3 5.5a4 4 0 0 1 6 0M6 8.2l1.3-1.3a1.8 1.8 0 0 0-2.6 0z" fill="none" stroke="#fff" stroke-width="1.2"/></svg>
      </div>
      <span>4:21 PM</span>
      <div class="status-right"><span>✱</span><span>100%</span><span class="battery"></span></div>
    </div>

    <header class="app-header">
      FC LINDENTAL-JUNIORS
      <svg class="settings-icon" viewBox="0 0 24 24" aria-label="Settings">
        <path fill="#c9cacd" d="M10.3 1.5h3.4l.5 2.7 1.8.8 2.3-1.6 2.4 2.4-1.6 2.3.8 1.8 2.6.5v3.4l-2.6.5-.8 1.8 1.6 2.3-2.4 2.4-2.3-1.6-1.8.8-.5 2.6h-3.4l-.5-2.6-1.8-.8-2.3 1.6-2.4-2.4 1.6-2.3-.8-1.8-2.6-.5v-3.4l2.6-.5.8-1.8-1.6-2.3 2.4-2.4 2.3 1.6 1.8-.8z"/>
        <circle cx="12" cy="12" r="3.6" fill="#141518"/>
      </svg>
    </header>

    <section class="weather-card">
      <div class="weather-info">
        <div class="weather-state">CLEAR</div>
        <svg class="cloud" viewBox="0 0 64 38"><path fill="#b9babd" d="M10 36a9 9 0 0 1-1-18 13 13 0 0 1 25-7 10 10 0 0 1 15 6 9.5 9.5 0 0 1 5 19z"/></svg>
        <div class="temp-line"><span class="temp">22°C</span><span class="feels">FEEL LIKE 21°C</span></div>
        <div class="precip">PRECIPITATION: 0%</div>
      </div>
      <div class="date-block">
        <div class="calendar">15</div>
        <div class="month">MAY</div>
        <div class="weekday">SATURDAY</div>
      </div>
    </section>

    <div class="session-time">17:30 PM</div>

    <section class="hero">
      <div class="ring ring-outer"></div>
      <div class="ring ring-mid"></div>
      <div class="ring ring-inner"></div>
      <div class="hero-art" role="img" aria-label="Illustration of a soccer player doing a bicycle kick"></div>
    </section>

    <section class="session-list">
      <div class="drill-row">
        <div><div class="drill-name">WARM UP</div><div class="drill-duration">20 MINUTE</div></div>
        <svg class="row-icon" viewBox="0 0 28 28"><g fill="none" stroke="#c9cacd" stroke-width="2" stroke-linecap="round"><path d="M5 13a9 9 0 0 1 16-5"/><path d="M23 15a9 9 0 0 1-16 5"/><path d="M21 3v5h-5"/><path d="M7 25v-5h5"/></g></svg>
      </div>
      <div class="drill-row">
        <div><div class="drill-name">4 <small>vs</small> 2</div><div class="drill-duration">25 MINUTE</div></div>
        <svg class="row-icon" viewBox="0 0 28 28"><g fill="none" stroke="#c9cacd" stroke-width="2" stroke-linecap="round"><path d="M5 13a9 9 0 0 1 16-5"/><path d="M23 15a9 9 0 0 1-16 5"/><path d="M21 3v5h-5"/><path d="M7 25v-5h5"/></g></svg>
      </div>
      <div class="drill-row">
        <div><div class="drill-name">OFFENSIVE 2 <small>vs</small> 1</div><div class="drill-duration">25 MINUTE</div></div>
        <svg class="row-icon" viewBox="0 0 28 28"><g fill="none" stroke="#c9cacd" stroke-width="2" stroke-linecap="round"><path d="M5 13a9 9 0 0 1 16-5"/><path d="M23 15a9 9 0 0 1-16 5"/><path d="M21 3v5h-5"/><path d="M7 25v-5h5"/></g></svg>
      </div>
      <div class="drill-row">
        <div><div class="drill-name">GAME 7 ON 7</div><div class="drill-duration">50 MINUTE</div></div>
        <svg class="row-icon" viewBox="0 0 28 28"><g fill="none" stroke="#c9cacd" stroke-width="2" stroke-linecap="round"><path d="M5 13a9 9 0 0 1 16-5"/><path d="M23 15a9 9 0 0 1-16 5"/><path d="M21 3v5h-5"/><path d="M7 25v-5h5"/></g></svg>
      </div>
      <div class="drill-row">
        <div class="nav-title">PLOMIX SKILLS</div>
        <svg class="row-icon" viewBox="0 0 28 28"><path d="M10 5l9 9-9 9" fill="none" stroke="#c9cacd" stroke-width="2" stroke-linecap="round"/></svg>
      </div>
      <div class="drill-row">
        <div class="nav-title">PLOMIX SKILLS</div>
        <svg class="row-icon" viewBox="0 0 28 28"><path d="M10 5l9 9-9 9" fill="none" stroke="#c9cacd" stroke-width="2" stroke-linecap="round"/></svg>
      </div>
    </section>

    <footer class="app-footer"><span class="footer-mark"></span></footer>
  </main>
</body>
</html>
```